Retailer of Global Mobile Credit Web Redesign

We need a professional redesign (photoshop only - no coding) of an existing ecommerce website. Currently the website runs on Wordpress with woocommerce. We would like to keep that setup.
The attached draft shows a very crude mockup of ideas for the homepage. These are ideas only - we value your creative suggestions. I have also attached a preliminary logo, but this will likely be changed, so please don't base your color choices on it.
The draft also gives you the URL of the current site.
One of the sites which has a design we like it globexsend.net.
The design is for ten pages - two of which are templates.
1. Homepage. Please see the attached draft for ideas. We like a darker picture with white lettering for the top of the page like Pennaroute.com. The photo is just to give color, it is not meant to capture the user's attention but just be a background.
2. Countries page (/countries/). We need an elegant, easily navigable way to show the countries where we offer credit and the operators we offer for that country. If you feel that it is better to delete the countries page and instead show that information when you click "countries" in the menu, then please design how the menu would look.
3. How It Works (/how-it-works/)
4. My Account (/account-info/) prior to logging in or registering)
5. My Account (/account-info) after logging in
6. Privacy (/privacy/). A basic page with text.
7. Checkout (/checkout/). You won't have access to this page but I've attached a screenshot that shows you all the elements of the checkout page.
8. /how-to-sell-phone-credit/
9. /ghana/ Your design for this page will be used as a template for all the country pages e.g. /antigua/ and /el-salvador/
10. /product/recharge-qvr-ghana/ Your design for this page will be used as a template for all operator pages e.g. /product/recharge-vexlo-ghana/ or /product/recharge-brindo-costa-rica/
Thank you in advance for your submissions. Be sure to let us know if you have any questions.
Reason: Hello, I was on holiday. I like the design very much and look forward to finalizing it.

```html
<!DOCTYPE html>
<html lang="en">
<head>
<meta charset="utf-8">
<title>Topline Traders Club – Mobile Credit</title>
<link href="https://fonts.googleapis.com/css2?family=Roboto:wght@300;400;500;700&family=Oswald:wght@300;400;500&display=swap" rel="stylesheet">
<style>
:root{
  --blue:#1b6fb5;
  --orange:#f0904f;
  --orange-text:#ee7d34;
  --ice:#dfeaf5;
  --ink:#333;
  --muted:#777;
  --footer:#1f1f1f;
  --footer-base:#151515;
  --footer-text:#c8c8c8;
  --white:#fff;
}
*{margin:0;padding:0;box-sizing:border-box}
html,body{width:719px;height:1200px;overflow:hidden;background:var(--white)}
body{position:relative;font-family:"Roboto",Arial,sans-serif;color:var(--ink)}
.abs{position:absolute}

/* header */
.brand{left:60px;top:18px;font-weight:700;font-size:19px;letter-spacing:.5px;color:var(--blue);display:flex;align-items:center;gap:6px}
.brand-dot{width:11px;height:11px;border-radius:50%;background:var(--blue)}
.topbar{right:59px;top:26px;display:flex;align-items:center;gap:7px;font-size:7px;color:#999}
.topbar .lang{color:var(--orange-text)}
.social-sq{width:13px;height:13px;border:1px solid #555;display:inline-block}
.social-sq + .social-sq{margin-left:-3px}

/* nav */
.nav{left:0;top:57px;width:719px;height:44px;background:var(--blue)}
.nav ul{list-style:none;position:absolute;left:59px;top:0;display:flex;height:44px}
.nav li{font-size:8px;color:var(--white);line-height:44px;padding:0 16px;letter-spacing:.2px}
.nav li.active{background:var(--orange)}
.search{left:508px;top:11px;width:152px;height:23px;background:var(--white);font-size:7px;color:#888;padding:0 7px;line-height:23px}
.search svg{position:absolute;right:7px;top:6px}

/* hero */
.hero{left:0;top:101px;width:719px;height:337px;background:radial-gradient(ellipse at 62% 25%,#8a5b3c 0%,#5a4034 35%,#2f2b2b 75%,#1f1e20 100%)}
.hero h1{position:absolute;left:0;width:719px;top:184px;text-align:center;font-family:"Oswald",sans-serif;font-weight:300;color:var(--white);font-size:28px;line-height:34px}
.hero h2{position:absolute;left:0;width:719px;top:221px;text-align:center;font-family:"Oswald",sans-serif;font-weight:300;color:var(--white);font-size:23px;line-height:30px}
.btn{background:var(--blue);color:var(--white);font-size:10px;font-weight:500;text-align:center;letter-spacing:.2px}
.hero .btn{position:absolute;left:286px;top:264px;width:146px;height:34px;line-height:34px}
.arrow{position:absolute;top:156px}

/* intro band */
.intro{left:0;top:438px;width:719px;height:83px;background:var(--orange)}
.intro p{position:absolute;left:59px;width:356px;font-size:6.5px;line-height:10.5px;color:var(--white)}
.intro .ask{position:absolute;left:447px;top:36px;font-size:9.5px;color:var(--white)}
.select{position:absolute;left:590px;top:30px;width:70px;height:24px;background:var(--white);font-size:7.5px;color:#333;padding-left:9px;line-height:24px}
.select svg{position:absolute;right:9px;top:10px}

/* features */
.features{left:0;top:521px;width:719px;height:245px;background:var(--ice)}
.feature{position:absolute;top:31px;width:180px;text-align:center}
.feature .ring{width:71px;height:71px;border-radius:50%;background:var(--white);margin:0 auto;display:flex;align-items:center;justify-content:center}
.feature h3{font-size:10px;font-weight:500;color:#333;margin-top:10px;letter-spacing:.2px}
.feature p{font-size:6.5px;line-height:10.5px;color:var(--muted);margin-top:8px;padding:0 6px}
.feature .more{margin:10px auto 0;display:block}
.wave{left:0;top:728px}

/* how it works */
.how-title{left:0;width:719px;top:756px;text-align:center;font-size:15px;font-weight:400;color:#333;letter-spacing:.3px}
.steps{left:0;top:793px}
.step-label{position:absolute;width:200px;text-align:center;font-size:10.5px;color:#333;line-height:14px;letter-spacing:.2px}
.how-btn{left:312px;top:955px;width:95px;height:32px;line-height:32px}

/* footer */
.footer{left:0;top:1018px;width:719px;height:157px;background:var(--footer);color:var(--footer-text)}
.footer h4{position:absolute;top:35px;font-size:11px;font-weight:400;color:var(--white);letter-spacing:.3px}
.footer .divider{position:absolute;top:34px;width:1px;height:116px;background:#3a3a3a}
.footer ul{list-style:none;position:absolute;font-size:8.5px;line-height:14.4px;color:var(--footer-text)}
.contact{position:absolute;left:183px;top:66px;font-size:8px;line-height:14.5px;color:var(--footer-text)}
.contact .ico{display:inline-block;width:7px;height:6px;background:var(--orange-text);margin-right:5px;border-radius:1px}
.newsletter p{position:absolute;left:369px;top:63px;width:170px;font-size:7px;line-height:13px;color:var(--footer-text)}
.news-input{position:absolute;left:369px;top:97px;width:140px;height:20px;background:var(--white);font-size:7px;color:#999;font-style:italic;line-height:20px;padding-left:7px}
.news-go{position:absolute;left:509px;top:97px;width:27px;height:20px;background:var(--orange-text);color:var(--white);font-size:7px;font-weight:500;text-align:center;line-height:20px}
.follow{position:absolute;left:595px;top:68px;list-style:none;font-size:8.5px;line-height:18.5px;color:var(--footer-text)}
.follow .mark{display:inline-block;width:6px;height:6px;background:var(--orange-text);margin-right:10px}
.base{left:0;top:1175px;width:719px;height:25px;background:var(--footer-base);font-size:7.5px;color:#888;text-align:center;line-height:25px}
</style>
</head>
<body>

<header>
  <div class="abs brand"><span class="brand-dot"></span>TOPLINE TRADERS CLUB</div>
  <div class="abs topbar">
    <span>Language: <span class="lang">English ▾</span></span>
    <svg width="18" height="8" viewBox="0 0 18 8"><circle cx="3" cy="2" r="1.8" fill="#555"/><path d="M0 8a3 3 0 0 1 6 0z" fill="#555"/><rect x="9" y="0" width="1" height="8" fill="#555"/><circle cx="14.5" cy="3.5" r="2.6" fill="none" stroke="#555" stroke-width="1.2"/><line x1="16.4" y1="5.4" x2="18" y2="7" stroke="#555" stroke-width="1.2"/></svg>
    <span style="width:8px"></span>
    <span class="social-sq"></span><span class="social-sq"></span><span class="social-sq"></span><span class="social-sq"></span>
  </div>
</header>

<nav class="abs nav">
  <ul>
    <li class="active">HOME</li>
    <li>COUNTRIES</li>
    <li>HOW IT WORKS</li>
    <li>MY ACCOUNT/JOIN FOR FREE</li>
    <li>CONTACT</li>
  </ul>
  <div class="abs search">Search...
    <svg width="11" height="11" viewBox="0 0 11 11"><circle cx="4.5" cy="4.5" r="3.6" fill="none" stroke="#333" stroke-width="1.5"/><line x1="7.2" y1="7.2" x2="10.3" y2="10.3" stroke="#333" stroke-width="1.7"/></svg>
  </div>
</nav>

<section class="abs hero" role="img" aria-label="Dimmed photo of a hand holding a mobile phone beside a cup of coffee">
  <svg class="arrow" style="left:45px" width="12" height="26" viewBox="0 0 12 26"><polyline points="11,1 1,13 11,25" fill="none" stroke="#fff" stroke-width="1.5"/></svg>
  <svg class="arrow" style="left:662px" width="12" height="26" viewBox="0 0 12 26"><polyline points="1,1 11,13 1,25" fill="none" stroke="#fff" stroke-width="1.5"/></svg>
  <h1>PURCHASE MOBILE PHONE CREDIT</h1>
  <h2>FOR YOURSELF OR YOUR FAMILY</h2>
  <div class="btn">GET STARTED FOR FREE</div>
</section>

<section class="abs intro">
  <p style="top:16px">Sending money is expensive. We want your money to go to your family—not a middle man. Founded by a former Harbor Aid Corps volunteer, the Topline Traders Club makes it easy to help families around the world.</p>
  <p style="top:45px">Simply buy airtime at wholesale prices for your family to resell at retail prices. When they make a sale, they collect the money you spent—plus a profit.</p>
  <div class="ask">Where does your family live?</div>
  <div class="select">Antigua
    <svg width="6" height="4" viewBox="0 0 6 4"><path d="M0 0h6L3 4z" fill="#333"/></svg>
  </div>
</section>

<section class="abs features">
  <div class="feature" style="left:53px">
    <div class="ring">
      <svg width="30" height="30" viewBox="0 0 30 30"><rect x="8" y="6" width="11" height="20" rx="1.5" fill="none" stroke="#1b6fb5" stroke-width="1.3"/><line x1="12" y1="23" x2="15" y2="23" stroke="#1b6fb5"/><path d="M21 4a5 5 0 0 1 4 4M21 1a8 8 0 0 1 7 7" fill="none" stroke="#1b6fb5" stroke-width="1.1"/></svg>
    </div>
    <h3>INSTANT RECHARGES</h3>
    <p>words which don't look even slightly believable. If you are going to use a passage orem Ipsum, you need to be sure there isn't anything embarrassing.</p>
    <svg class="more" width="11" height="11" viewBox="0 0 11 11"><circle cx="5.5" cy="5.5" r="4.8" fill="none" stroke="#1b6fb5"/><path d="M5.5 3v5M3 5.5h5" stroke="#1b6fb5"/></svg>
  </div>
  <div class="feature" style="left:274px">
    <div class="ring">
      <svg width="36" height="36" viewBox="0 0 36 36" fill="none" stroke="#1b6fb5" stroke-width="1.4"><circle cx="18" cy="18" r="16"/><ellipse cx="18" cy="18" rx="7" ry="16"/><line x1="2" y1="18" x2="34" y2="18"/><path d="M5 10h26M5 26h26"/><line x1="18" y1="2" x2="18" y2="34"/></svg>
    </div>
    <h3>WORLDWIDE SERVICES</h3>
    <p>The Extremes of Good and Evil) by Ostrevo, written in 45 BC. This book is a treatise on the theory of ethics, very popular during the.</p>
    <svg class="more" width="11" height="11" viewBox="0 0 11 11"><circle cx="5.5" cy="5.5" r="4.8" fill="none" stroke="#1b6fb5"/><path d="M5.5 3v5M3 5.5h5" stroke="#1b6fb5"/></svg>
  </div>
  <div class="feature" style="left:494px">
    <div class="ring">
      <svg width="34" height="30" viewBox="0 0 34 30" fill="none" stroke="#1b6fb5" stroke-width="1.4"><circle cx="19" cy="4" r="2.5" fill="#1b6fb5" stroke="none"/><ellipse cx="17" cy="18" rx="12" ry="8"/><line x1="14" y1="26" x2="14" y2="29"/><line x1="21" y1="26" x2="21" y2="29"/><line x1="14" y1="12" x2="20" y2="12"/></svg>
    </div>
    <h3>TRANSPARENT PRICES</h3>
    <p>Dignissimos ducimus qui blanditiis praesentium voluptatum deleniti atque corrupti quos dolores quas molestias excepturi sint occaecati.</p>
    <svg class="more" width="11" height="11" viewBox="0 0 11 11"><circle cx="5.5" cy="5.5" r="4.8" fill="none" stroke="#1b6fb5"/><path d="M5.5 3v5M3 5.5h5" stroke="#1b6fb5"/></svg>
  </div>
</section>

<svg class="abs wave" width="719" height="40" viewBox="0 0 719 40">
  <path d="M0 10Q360 -10 719 10V40H0z" fill="#e4e4e4"/>
  <path d="M0 18Q360 -2 719 18V40H0z" fill="#fff"/>
</svg>

<section>
  <h2 class="abs how-title">HOW IT WORKS</h2>
  <svg class="abs steps" width="719" height="100" viewBox="0 0 719 100">
    <line x1="183" y1="48" x2="314" y2="48" stroke="#1b6fb5" stroke-width="3"/>
    <line x1="404" y1="48" x2="536" y2="48" stroke="#1b6fb5" stroke-width="3"/>
    <g fill="#fff" stroke="#1b6fb5" stroke-width="2">
      <circle cx="138" cy="48" r="45"/><circle cx="359" cy="48" r="45"/><circle cx="581" cy="48" r="45"/>
    </g>
    <g fill="#ee7d34" font-family="Oswald, sans-serif" font-size="36" font-weight="500" text-anchor="middle">
      <text x="138" y="61">1</text><text x="359" y="61">2</text><text x="581" y="61">3</text>
    </g>
  </svg>
  <div class="step-label" style="left:38px;top:905px">JOIN FOR FREE</div>
  <div class="step-label" style="left:260px;top:905px">CHOOSE&nbsp; YOUR&nbsp; RECHARGE</div>
  <div class="step-label" style="left:480px;top:902px">PAY SECURELY WITH<br>YOUR CARD VIA PAYNEST</div>
  <div class="abs btn how-btn">LEARN MORE</div>
</section>

<footer class="abs footer">
  <h4 style="left:60px">MARIANNA</h4>
  <ul style="left:60px;top:64px">
    <li>Home</li><li>Countries</li><li>How It Works</li><li>My Account</li><li>&nbsp;Contact</li>
  </ul>
  <div class="divider" style="left:158px"></div>

  <h4 style="left:183px">CONTACT US</h4>
  <div class="contact">
    Norvale Systems PO Box 2207<br>Kestrel Bay, 40518<br>
    <span class="ico"></span>info@toplineclub.com<br>
    <span class="ico"></span>671.555.0142
  </div>
  <div class="divider" style="left:337px"></div>

  <div class="newsletter">
    <h4 style="left:369px">SIGN TO NEWSLETTER</h4>
    <p>Join our confidential network and be the first job listings for Connecticut military.</p>
    <div class="news-input">Name...</div>
    <div class="news-go">GO!</div>
  </div>
  <div class="divider" style="left:572px"></div>

  <h4 style="left:595px">FOLLOW US</h4>
  <ul class="follow">
    <li><span class="mark"></span>Friendwall</li>
    <li><span class="mark"></span>Chirper</li>
    <li><span class="mark"></span>Snapgram</li>
  </ul>
</footer>

<div class="abs base">© 2016 Toplineclub.com. Toplineclub.com is an independent airtime distributor. All trademarks are property of their respective owners. | Privacy | Contact</div>

</body>
</html>
```